Website Design for an Exciting, Fun & Premium Cannabis Company

Website will be designed and implemented for Wordpress with the ability to connect Leafroute Bazaar.
Looking to build trust with website visitors with engaging, exciting & informative content that will drive business to local dispensaries within the state of Oklahoma.
The website will embody excitement, fun, enthusiasm and make the visitor identify with the content and emphasize with a fun life they can have or believe they can have by using our products & will allow for super charged SEO and other digital marketing and advertising strategies and tactics used to increase discovery, awareness, and conversion.

Target Market(s)

Male/Female Ages 21-45

Coding

Coded - Design and coding required

Number of Pages Required

5+ page

Font styles to use
Sans Serif

Requirements
Must have
• Please see attached document for this information
Nice to have
Should not have

```html
<!DOCTYPE html>
<html lang="en">
<head>
<meta charset="utf-8">
<title>Halvane — Premium Cannabis Company</title>
<link href="https://fonts.googleapis.com/css2?family=Mulish:wght@400;600;700;800;900&family=Roboto:ital,wght@0,400;0,500;0,700;1,400&display=swap" rel="stylesheet">
<style>
:root{
  --lime:#a4cd2e;
  --green:#5cc433;
  --green-dark:#3ea72c;
  --ink:#262626;
  --text:#5b5b5b;
  --muted:#8a8a8a;
  --line:#e4e4e4;
  --white:#fff;
  --footer:#f7f7f7;
  --blue:#1e9ad6;
}
*{box-sizing:border-box;margin:0;padding:0}
html,body{width:1200px;height:3903px;overflow:hidden}
body{position:relative;background:var(--white);font-family:"Roboto",Arial,sans-serif;color:var(--text)}
.abs{position:absolute}
h1,h2,h3{font-family:"Mulish",Arial,sans-serif;color:var(--ink)}

/* top bar */
.topbar{left:0;top:0;width:1200px;height:48px;background:var(--lime);color:#2b3a0e;font-size:14px}
.topbar .hours{left:110px;top:15px;display:flex;gap:7px;align-items:center}
.topbar .phone{right:110px;top:15px;display:flex;gap:7px;align-items:center}

/* nav */
.nav{left:0;top:48px;width:1200px;height:105px;background:var(--white)}
.brand{display:flex;align-items:center;gap:8px;font-family:"Mulish",sans-serif;font-weight:900;color:var(--blue)}
.nav .brand{left:110px;top:34px;font-size:30px}
.brand .dot{width:16px;height:16px;border-radius:50%;background:var(--green)}
.menu{left:375px;top:46px;display:flex;gap:47px;font-size:14.5px;font-weight:500;color:var(--ink);letter-spacing:.3px}
.menu .active{color:var(--green);position:relative}
.menu .active::after{content:"";position:absolute;left:0;right:0;bottom:-9px;height:3px;background:var(--green)}
.lang{left:1001px;top:45px;font-size:14px;color:var(--ink);display:flex;gap:8px;align-items:center}
.lang .flag{width:34px;height:34px;border-radius:50%;background:linear-gradient(#c8283a 0 50%,#f2f2f2 50%);box-shadow:inset 12px 12px 0 -2px #2f3c8c}

/* hero */
.hero{left:0;top:153px;width:1200px;height:618px;background:linear-gradient(100deg,#efe6dc 0%,#e8dccf 30%,#c99f78 55%,#9d8f6c 72%,#c4ad8a 100%)}
.hero .copy{left:83px;top:152px;line-height:.9;font-family:"Mulish",Arial,sans-serif;color:#2b2b2b}
.hero .copy .small{font-size:52px;font-weight:700}
.hero .copy .big{font-size:72px;font-weight:900;letter-spacing:.5px}
.btn{display:inline-flex;align-items:center;justify-content:center;border-radius:30px;background:linear-gradient(90deg,var(--green),var(--lime));color:var(--white);font-family:"Mulish",sans-serif;font-weight:800;font-size:14.5px;letter-spacing:.5px}
.hero .btn{left:87px;top:409px;width:164px;height:48px}
.arrows{display:flex;gap:10px}
.arrow{width:34px;height:34px;border-radius:50%;display:flex;align-items:center;justify-content:center;background:#e6e6e6;color:#333}
.arrow.on{background:var(--lime);color:#2b3a0e}
.hero .arrows{left:87px;top:519px}

/* collections */
.section-title{font-size:36px;font-weight:700}
.collections .section-title{left:111px;top:860px}
.collections .arrows{left:989px;top:870px}
.card{width:316px;height:264px;border:3px solid #dedede;border-radius:6px;overflow:hidden;background:linear-gradient(#fff 0 80%,#e9e9e9)}
.card .tools{left:33px;top:20px;display:flex;gap:13px}
.card .tool{width:34px;height:34px;border-radius:50%;border:1.5px solid #555;display:flex;align-items:center;justify-content:center;background:#fff}
.card .name{right:33px;top:24px;font-weight:700;font-size:16px;color:var(--ink)}
.card .photo{left:20px;top:70px;width:270px;height:160px;border-radius:6px}
.card .add{left:73px;top:105px;width:160px;height:46px}

/* promo */
.promo{left:0;top:1600px;width:1200px;height:401px;background:var(--lime);overflow:hidden}
.promo .photo{left:0;top:0;width:600px;height:401px;background:linear-gradient(90deg,#7cbf3c,#4aa83a 45%,#8cc435 85%,var(--lime))}
.promo .eyebrow{left:636px;top:112px;font-size:38px;font-weight:800;color:var(--white);letter-spacing:.5px}
.promo .offer{left:636px;top:155px;color:var(--white);font-family:"Mulish",sans-serif;display:flex;align-items:baseline;gap:8px}
.promo .offer b{font-size:80px;font-weight:900;font-style:italic}
.promo .offer span{font-size:38px;font-weight:800}
.promo .btn{left:638px;top:247px;width:144px;height:46px;background:var(--green-dark)}

/* about */
.about .photo{left:600px;top:2001px;width:600px;height:419px;background:linear-gradient(135deg,#e8eef0,#cfd9dc 40%,#b8c9a4 70%,#e3e8d6)}
.about h2{left:111px;top:2068px;font-size:42px;font-weight:800;letter-spacing:.5px}
.about p{left:111px;top:2130px;width:425px;font-size:14.2px;line-height:25.6px;color:var(--text)}
.about .outline{left:108px;top:2333px;width:181px;height:50px;border:3px solid var(--green);border-radius:30px;color:var(--green);font-family:"Mulish",sans-serif;font-weight:800;font-size:14.5px;display:flex;align-items:center;justify-content:center;gap:6px}

/* testimonials */
.testi-title{left:0;top:2506px;width:1200px;text-align:center;font-size:40px;font-weight:800}
.quote{width:312px;height:190px;border:1.5px solid var(--line);border-top:3px solid var(--green);border-radius:14px}
.quote .avatar{left:112px;top:-45px;width:88px;height:88px;border-radius:50%;background:linear-gradient(#d7d7d7,#8d8d8d);border:3px solid #fff}
.quote p{left:25px;top:70px;width:262px;text-align:center;font-style:italic;font-size:15px;line-height:22px;color:var(--text)}
.who{width:312px;text-align:center;font-size:14.5px;color:var(--ink);font-weight:500}
.who small{font-size:9px;color:#555}
.who .stars{color:#f2c11b;font-size:13px;letter-spacing:1px;margin-top:4px}

/* blog */
.blog{left:0;top:2988px;width:1200px;height:517px;background:linear-gradient(120deg,#6cc63f,#45b73a 50%,#52bd3c)}
.blog h2{left:0;top:84px;width:1200px;text-align:center;color:var(--white);font-size:40px;font-weight:800}
.post .img{width:309px;height:214px}
.post .date{left:12px;top:140px;width:52px;height:58px;background:#fff;text-align:center;font-family:"Mulish",sans-serif;color:#222;font-weight:700;line-height:1}
.post .date span{display:block;font-size:15px;margin-top:7px}
.post .date b{display:block;font-size:20px;font-weight:800;margin-top:3px}
.post h3{top:236px;width:320px;color:var(--white);font-size:22px;font-weight:800;line-height:28px}

/* footer */
.footer{left:0;top:3505px;width:1200px;height:398px;background:var(--footer)}
.footer .brand{left:129px;top:110px;font-size:34px}
.socials{left:139px;top:243px;display:flex;gap:10px}
.socials i{width:30px;height:30px;border-radius:50%;display:block}
.fcol{top:100px}
.fcol h4{font-family:"Roboto",sans-serif;font-weight:700;color:var(--ink);font-size:16px;margin-bottom:19px}
.fcol li{list-style:none;font-size:13.5px;color:var(--muted);line-height:25.7px}
.contact-item{display:flex;gap:10px;margin-bottom:16px}
.contact-item svg{flex:none;margin-top:2px}
.contact-item b{display:block;font-size:11.5px;color:var(--ink)}
.contact-item span{font-size:13px;color:var(--muted);line-height:18px;display:block;width:200px}
.footer .rule{left:110px;top:324px;width:980px;height:1px;background:var(--line)}
.footer .copy{left:0;top:347px;width:1200px;text-align:center;font-size:14px;color:#555}
.footer .up{left:1107px;top:307px;width:34px;height:34px;border-radius:50%;background:var(--green);display:flex;align-items:center;justify-content:center}
.footer .tag{left:1159px;top:361px;font-size:11px;color:#777}
</style>
</head>
<body>

<header>
  <div class="abs topbar">
    <div class="abs hours"><svg width="12" height="12" viewBox="0 0 12 12"><circle cx="6" cy="6" r="5" fill="none" stroke="#2b3a0e" stroke-width="1.5"/><path d="M6 3v3l2 1" stroke="#2b3a0e" stroke-width="1.3" fill="none"/></svg>Monday - Friday 8:00 AM - 5:00 PM CT</div>
    <div class="abs phone"><svg width="12" height="12" viewBox="0 0 24 24"><path fill="#2b3a0e" d="M6.6 10.8a15 15 0 006.6 6.6l2.2-2.2c.3-.3.7-.4 1-.2 1.1.4 2.3.6 3.6.6.6 0 1 .4 1 1V20c0 .6-.4 1-1 1A17 17 0 013 4c0-.6.4-1 1-1h3.5c.6 0 1 .4 1 1 0 1.3.2 2.5.6 3.6.1.3 0 .7-.2 1z"/></svg>Phone : +1 888 888 8888</div>
  </div>
  <nav class="abs nav">
    <div class="abs brand"><i class="dot"></i>Halvane</div>
    <div class="abs menu"><span class="active">HOME</span><span>COMMUNITY</span><span>SHOP</span><span>WHOLESALE</span><span>CONTACT</span></div>
    <div class="abs lang">Eng <svg width="8" height="5" viewBox="0 0 8 5"><path d="M0 0h8L4 5z" fill="#333"/></svg><span class="flag"></span></div>
  </nav>
</header>

<section class="abs hero" role="img" aria-label="Flat lay of cannabis leaves, heart-shaped candle holders, stones, a dropper bottle of oil and bowls of clay and seeds on a wooden table">
  <div class="abs copy">
    <div class="small">We are a</div>
    <div class="big">Premium</div>
    <div class="big">Cannabis</div>
    <div class="small">Company.</div>
  </div>
  <a class="abs btn">GET STARTED</a>
  <div class="abs arrows">
    <span class="arrow"><svg width="8" height="10" viewBox="0 0 8 10"><path d="M6 1L2 5l4 4" stroke="#333" stroke-width="1.6" fill="none"/></svg></span>
    <span class="arrow on"><svg width="8" height="10" viewBox="0 0 8 10"><path d="M2 1l4 4-4 4" stroke="#333" stroke-width="1.6" fill="none"/></svg></span>
  </div>
</section>

<section class="collections">
  <h2 class="abs section-title">Our Collections</h2>
  <div class="abs arrows">
    <span class="arrow"><svg width="8" height="10" viewBox="0 0 8 10"><path d="M6 1L2 5l4 4" stroke="#333" stroke-width="1.6" fill="none"/></svg></span>
    <span class="arrow on"><svg width="8" height="10" viewBox="0 0 8 10"><path d="M2 1l4 4-4 4" stroke="#333" stroke-width="1.6" fill="none"/></svg></span>
  </div>

  <div class="abs card" style="left:109px;top:956px">
    <div class="abs tools"><span class="tool"><svg width="14" height="13" viewBox="0 0 24 22"><path d="M12 21S2 14 2 7.5A5 5 0 0112 5a5 5 0 0110 2.5C22 14 12 21 12 21z" fill="none" stroke="#444" stroke-width="2"/></svg></span><span class="tool"><svg width="14" height="13" viewBox="0 0 24 22"><path d="M1 2h4l3 12h12l3-9H7" fill="none" stroke="#444" stroke-width="2.4"/><circle cx="9" cy="19" r="2" fill="#444"/><circle cx="19" cy="19" r="2" fill="#444"/></svg></span></div>
    <div class="abs name">Product Tittle</div>
    <div class="abs photo" role="img" aria-label="Jar of dried flower beside loose ground herb" style="background:linear-gradient(135deg,#e9e0ea,#d8cdc0 60%,#f4f0ea)"></div>
  </div>
  <div class="abs card" style="left:442px;top:956px">
    <div class="abs tools"><span class="tool"><svg width="14" height="13" viewBox="0 0 24 22"><path d="M12 21S2 14 2 7.5A5 5 0 0112 5a5 5 0 0110 2.5C22 14 12 21 12 21z" fill="none" stroke="#444" stroke-width="2"/></svg></span><span class="tool"><svg width="14" height="13" viewBox="0 0 24 22"><path d="M1 2h4l3 12h12l3-9H7" fill="none" stroke="#444" stroke-width="2.4"/><circle cx="9" cy="19" r="2" fill="#444"/><circle cx="19" cy="19" r="2" fill="#444"/></svg></span></div>
    <div class="abs name">Product Tittle</div>
    <div class="abs photo" role="img" aria-label="Amber dropper bottle with a cannabis leaf" style="background:linear-gradient(180deg,#fafafa,#e4eddc)"></div>
  </div>
  <div class="abs card" style="left:776px;top:956px">
    <div class="abs tools"><span class="tool"><svg width="14" height="13" viewBox="0 0 24 22"><path d="M12 21S2 14 2 7.5A5 5 0 0112 5a5 5 0 0110 2.5C22 14 12 21 12 21z" fill="none" stroke="#444" stroke-width="2"/></svg></span><span class="tool"><svg width="14" height="13" viewBox="0 0 24 22"><path d="M1 2h4l3 12h12l3-9H7" fill="none" stroke="#444" stroke-width="2.4"/><circle cx="9" cy="19" r="2" fill="#444"/><circle cx="19" cy="19" r="2" fill="#444"/></svg></span></div>
    <div class="abs name">Product Tittle</div>
    <div class="abs photo" role="img" aria-label="Chocolate edibles with green filling and cannabis leaves" style="background:linear-gradient(180deg,#fafafa,#ebe2dc)"></div>
  </div>
  <div class="abs card" style="left:109px;top:1239px">
    <div class="abs tools"><span class="tool"><svg width="14" height="13" viewBox="0 0 24 22"><path d="M12 21S2 14 2 7.5A5 5 0 0112 5a5 5 0 0110 2.5C22 14 12 21 12 21z" fill="none" stroke="#444" stroke-width="2"/></svg></span><span class="tool"><svg width="14" height="13" viewBox="0 0 24 22"><path d="M1 2h4l3 12h12l3-9H7" fill="none" stroke="#444" stroke-width="2.4"/><circle cx="9" cy="19" r="2" fill="#444"/><circle cx="19" cy="19" r="2" fill="#444"/></svg></span></div>
    <div class="abs name">Product Tittle</div>
    <div class="abs photo" role="img" aria-label="Oil bottles and a cream jar with a cannabis leaf" style="background:linear-gradient(180deg,#fdf6e0,#f2e2a8)"></div>
  </div>
  <div class="abs card" style="left:442px;top:1239px;background:linear-gradient(#e3f6ea,#cdeedb)">
    <div class="abs tools"><span class="tool"><svg width="14" height="13" viewBox="0 0 24 22"><path d="M12 21S2 14 2 7.5A5 5 0 0112 5a5 5 0 0110 2.5C22 14 12 21 12 21z" fill="none" stroke="#444" stroke-width="2"/></svg></span><span class="tool"><svg width="14" height="13" viewBox="0 0 24 22"><path d="M1 2h4l3 12h12l3-9H7" fill="none" stroke="#444" stroke-width="2.4"/><circle cx="9" cy="19" r="2" fill="#444"/><circle cx="19" cy="19" r="2" fill="#444"/></svg></span></div>
    <div class="abs name">Product Tittle</div>
    <div class="abs photo" role="img" aria-label="Jar of balm with a soft cannabis leaf on a mint background" style="background:linear-gradient(180deg,#e3f6ea,#d3efdc)"></div>
    <a class="abs btn add">ADD TO CART</a>
  </div>
  <div class="abs card" style="left:776px;top:1239px">
    <div class="abs tools"><span class="tool"><svg width="14" height="13" viewBox="0 0 24 22"><path d="M12 21S2 14 2 7.5A5 5 0 0112 5a5 5 0 0110 2.5C22 14 12 21 12 21z" fill="none" stroke="#444" stroke-width="2"/></svg></span><span class="tool"><svg width="14" height="13" viewBox="0 0 24 22"><path d="M1 2h4l3 12h12l3-9H7" fill="none" stroke="#444" stroke-width="2.4"/><circle cx="9" cy="19" r="2" fill="#444"/><circle cx="19" cy="19" r="2" fill="#444"/></svg></span></div>
    <div class="abs name">Product Tittle</div>
    <div class="abs photo" role="img" aria-label="Two amber dropper bottles on a green leaf" style="background:linear-gradient(180deg,#f2f2f2,#dfe6d8)"></div>
  </div>
</section>

<section class="abs promo">
  <div class="abs photo" role="img" aria-label="Woman in glasses holding a dropper bottle of oil against a green backdrop"></div>
  <h2 class="abs eyebrow">PREMIUM CANNABIS</h2>
  <div class="abs offer"><b>75%</b><span>OFFER</span></div>
  <a class="abs btn">SHOP NOW</a>
</section>

<section class="about">
  <h2 class="abs">ABOUT US</h2>
  <p class="abs">Lorem ipsum dolor sit amet, consectetur adipiscing elit, sed do eiusmod tempor incididunt ut labore et dolore magna aliqua. Ut enim ad minim veniam, quis nostrud exercitation ullamco laboris nisi ut aliquip ex ea commodo consequat. Duis aute irure dolor in reprehenderit in voluptate velit esse cillum dolore eu fugiat nulla pariatur. Excepteur sint occaecat cupidatat non proident, sunt in culpa qui officia deserunt mollit anim id est laborum.</p>
  <a class="abs outline">LEARN MORE <svg width="13" height="13" viewBox="0 0 14 14"><circle cx="7" cy="7" r="7" fill="#5cc433"/><path d="M4 7h5M7 4.5L9.5 7 7 9.5" stroke="#fff" stroke-width="1.6" fill="none"/></svg></a>
  <div class="abs photo" role="img" aria-label="Gloved hands filling a vial with oil from a dropper beside cannabis leaves and test tubes"></div>
</section>

<section class="testimonials">
  <h2 class="abs testi-title">What Our clients say?</h2>
  <div class="abs quote" style="left:110px;top:2639px">
    <div class="abs avatar" role="img" aria-label="Client portrait"></div>
    <p class="abs">Lorem ipsum dolor sit consectetur adipiscing elit, sed do eiusmod tempor incididunt ut labore et dolore magna aliqua. Ut enim ad minim</p>
  </div>
  <div class="abs quote" style="left:444px;top:2639px">
    <div class="abs avatar" role="img" aria-label="Client portrait"></div>
    <p class="abs">Lorem ipsum dolor sit consectetur adipiscing elit, sed do eiusmod tempor incididunt ut labore et dolore magna aliqua. Ut enim ad minim</p>
  </div>
  <div class="abs quote" style="left:778px;top:2639px">
    <div class="abs avatar" role="img" aria-label="Client portrait"></div>
    <p class="abs">Lorem ipsum dolor sit consectetur adipiscing elit, sed do eiusmod tempor incididunt ut labore et dolore magna aliqua. Ut enim ad minim</p>
  </div>
  <div class="abs who" style="left:110px;top:2852px">Dana Whitlow, <small>Chairman RHC</small><div class="stars">★★★★★</div></div>
  <div class="abs who" style="left:444px;top:2852px">Lena Ortiz, <small>Project Manager</small><div class="stars">★★★★★</div></div>
  <div class="abs who" style="left:778px;top:2852px">Sam Keller, <small>Chairman RHC</small><div class="stars">★★★★★</div></div>
</section>

<section class="abs blog">
  <h2 class="abs">Latest Blog</h2>
  <article class="abs post" style="left:112px;top:160px">
    <div class="abs img" role="img" aria-label="Scientists in lab coats reviewing a clipboard" style="background:linear-gradient(#cfe0ee,#e9f0f5 50%,#b7cde0)"></div>
    <div class="abs date"><span>May</span><b>06</b></div>
    <h3 class="abs" style="left:-3px">Lorem ipsum dolor sit amet, consectetur adip</h3>
  </article>
  <article class="abs post" style="left:445px;top:160px">
    <div class="abs img" role="img" aria-label="Woman in a sun hat among tall cannabis plants" style="background:linear-gradient(#e6ece8,#4c7a3a 40%,#2e5a26 75%,#d9a0a0)"></div>
    <div class="abs date"><span>May</span><b>06</b></div>
    <h3 class="abs" style="left:-2px">Lorem ipsum dolor sit amet, consectetur adip</h3>
  </article>
  <article class="abs post" style="left:779px;top:160px">
    <div class="abs img" role="img" aria-label="Close-up of a cannabis bud against a blue backdrop" style="background:linear-gradient(160deg,#eef0ee,#a8b8c8 40%,#1e3e6e 75%,#0c1e44)"></div>
    <div class="abs date"><span>May</span><b>06</b></div>
    <h3 class="abs" style="left:-2px">Lorem ipsum dolor sit amet, consectetur adip</h3>
  </article>
</section>

<footer class="abs footer">
  <div class="abs brand"><i class="dot"></i>Halvane</div>
  <div class="abs socials"><i style="background:#3b5998"></i><i style="background:#1da1f2"></i><i style="background:#dd4b39"></i><i style="background:#b0379a"></i></div>
  <div class="abs fcol" style="left:409px"><h4>Quick Links</h4><ul><li>Home</li><li>Community</li><li>Shop</li><li>Wholesale</li><li>Contact</li></ul></div>
  <div class="abs fcol" style="left:603px"><h4>About Company</h4><ul><li>Mission</li><li>Customer Satisfaction</li><li>Shipping &amp; Return Policy</li><li>Privacy Policy</li><li>Terms of Service</li></ul></div>
  <div class="abs fcol" style="left:871px"><h4>Contact Us</h4>
    <div class="contact-item"><svg width="13" height="13" viewBox="0 0 24 24"><path fill="#5cc433" d="M6.6 10.8a15 15 0 006.6 6.6l2.2-2.2c.3-.3.7-.4 1-.2 1.1.4 2.3.6 3.6.6.6 0 1 .4 1 1V20c0 .6-.4 1-1 1A17 17 0 013 4c0-.6.4-1 1-1h3.5c.6 0 1 .4 1 1 0 1.3.2 2.5.6 3.6.1.3 0 .7-.2 1z"/></svg><div><b>Phone</b><span>+888 888 8888</span></div></div>
    <div class="contact-item"><svg width="13" height="11" viewBox="0 0 14 11"><rect width="14" height="11" rx="1" fill="#5cc433"/><path d="M1 1l6 5 6-5" stroke="#fff" stroke-width="1.3" fill="none"/></svg><div><b>Email</b><span>info@halvanelabs.com</span></div></div>
    <div class="contact-item"><svg width="11" height="14" viewBox="0 0 12 16"><path d="M6 0a6 6 0 00-6 6c0 4.5 6 10 6 10s6-5.5 6-10a6 6 0 00-6-6z" fill="#5cc433"/><circle cx="6" cy="6" r="2.2" fill="#fff"/></svg><div><b>Location</b><span>Lorem ipsum dolor sit amet, con elit, sed</span></div></div>
  </div>
  <div class="abs rule"></div>
  <div class="abs copy">2021 Copyright - Company name| All Rights Reserved</div>
  <div class="abs up"><svg width="12" height="8" viewBox="0 0 12 8"><path d="M1 7l5-5 5 5" stroke="#fff" stroke-width="2" fill="none"/></svg></div>
  <div class="abs tag">C38</div>
</footer>

</body>
</html>
```